I need a new business card design for my pharmacy.

I need a business card design. I will include my logo.
The card needs to be readable. I prefer to have my logo on one side along with my website, the other side includes the other information. Please use combination of black, neon green, white, and silver. This needs to catch the eye but yet be clearly visible and legible. Thanks

Industry/Entity Type

Pharmacy

Contact Information for Business Card

It needs to have the following information listed:
Mel's Apothecary Owner/Pharm D.
7134 North Brook Lane
Sioux Falls, SD 57231
Phone 605-318-6207
Fax 605-318-6209
email: mel@melsapothecary-example.com
www.melsapothecary-example.com
Store hours Monday-Friday 8 am- 7 pm
Saturday 8 am- 12 pm
Sunday Closed
Please utilize the colors black, white, and neon green, maybe silver.

Requirements
Must have
• It needs to be easily readable!
Nice to have
• It should catch the eye.
Should not have
• Do not use any other colors except listed: black, neon green, white, & silver.

```html
<!DOCTYPE html>
<html lang="en">
<head>
<meta charset="utf-8">
<title>Mel's Apothecary – Business Card</title>
<link href="https://fonts.googleapis.com/css2?family=Oxygen:wght@300;400;700&display=swap" rel="stylesheet">
<style>
  :root {
    --backdrop: #333333;
    --neon-green: #75c045;
    --ink: #231f20;
    --white: #ffffff;
  }
  * { margin: 0; padding: 0; box-sizing: border-box; }
  html, body {
    width: 1200px; height: 1200px; overflow: hidden;
    background: var(--backdrop);
    font-family: "Oxygen", "Helvetica Neue", Arial, sans-serif;
  }
  .canvas { position: relative; width: 1200px; height: 1200px; }

  .card {
    position: absolute; left: 241px; width: 718px; height: 431px;
    overflow: hidden;
    box-shadow: 0 2px 6px rgba(0,0,0,0.35);
  }
  .card--front { top: 116px; background: var(--neon-green); }
  .card--back { top: 654px; background: var(--white); }

  .brand { position: absolute; display: flex; align-items: center; }
  .brand__dot { border-radius: 50%; flex: none; }
  .brand__rule { width: 2px; flex: none; }
  .brand__name {
    font-weight: 700; letter-spacing: -1.6px; white-space: nowrap; line-height: 1;
  }

  .card--front .brand { left: 150px; top: 172px; height: 80px; }
  .card--front .brand__dot { width: 54px; height: 54px; background: var(--white); margin-right: 44px; }
  .card--front .brand__rule { height: 80px; background: var(--white); margin-right: 22px; }
  .card--front .brand__name { color: var(--white); font-size: 41px; }

  .card--back .brand { left: 150px; top: 112px; height: 87px; }
  .card--back .brand__dot { width: 58px; height: 58px; background: var(--ink); margin-right: 64px; }
  .card--back .brand__rule { height: 87px; background: var(--ink); margin-right: 24px; }
  .card--back .brand__name { color: var(--ink); font-size: 43px; }

  .info-band {
    position: absolute; left: 0; top: 242px; width: 718px; height: 189px;
    background: var(--neon-green); color: var(--white);
  }
  .contact { position: absolute; left: 63px; top: 42px; }
  .contact__title {
    font-size: 18px; font-weight: 700; letter-spacing: -0.7px;
    margin: 0 0 6px 4px; white-space: nowrap;
  }
  .contact__line {
    font-size: 12px; line-height: 19px; letter-spacing: -0.5px; white-space: nowrap; font-weight: 300;
  }
  .contact__line b { font-weight: 700; }
  .contact__line--web { font-size: 11px; letter-spacing: -0.55px; }

  .hours {
    position: absolute; left: 479px; top: 58px;
    border-left: 2px solid var(--white); padding-left: 11px;
    font-size: 13.5px; font-weight: 700; line-height: 18.8px; white-space: nowrap;
  }
</style>
</head>
<body>
<div class="canvas">

  <section class="card card--front">
    <div class="brand">
      <span class="brand__dot"></span>
      <span class="brand__rule"></span>
      <span class="brand__name">Mel's Apothecary</span>
    </div>
  </section>

  <section class="card card--back">
    <div class="brand">
      <span class="brand__dot"></span>
      <span class="brand__rule"></span>
      <span class="brand__name">Mel's Apothecary</span>
    </div>

    <div class="info-band">
      <div class="contact">
        <p class="contact__title">Mel's Apothecary Owner/Pharm D.</p>
        <p class="contact__line">adress: <b>7134 North Brook Lane</b> / <b>Sioux Falls, SD 57231</b></p>
        <p class="contact__line">phone: <b>605-318-6207</b> / fax: <b>605-318-6209</b></p>
        <p class="contact__line contact__line--web">mail: <b>mel@melsapothecary-example.com</b> / web: <b>www.melsapothecary-example.com</b></p>
      </div>
      <div class="hours">
        <p>Store hours</p>
        <p>Monday-Friday 8 am- 7 pm</p>
        <p>Saturday 8 am- 12 pm</p>
        <p>Sunday Closed</p>
      </div>
    </div>
  </section>

</div>
</body>
</html>
```